Design some Business Cards for Torvique

I am wanting business cards designed. I will supply Logo and other details.
Needs to be simple and catch. All file formats for print must be supplied

```html
<!DOCTYPE html>
<html lang="en">
<head>
<meta charset="utf-8">
<title>Torvique Business Card</title>
<link rel="stylesheet" href="https://fonts.googleapis.com/css2?family=Open+Sans:wght@400;600&display=swap">
<style>
  :root {
    --backdrop: #c6c9b0;
    --card-white: #ffffff;
    --accent-blue: #34ace3;
    --panel-grey: #474747;
    --ink-dark: #1f1f1f;
    --ink-light: #ffffff;
    --brand-blue: #35a9df;
  }
  html, body {
    margin: 0;
    padding: 0;
    width: 1200px;
    height: 900px;
    overflow: hidden;
    background: var(--backdrop);
    font-family: "Open Sans", Arial, sans-serif;
  }
  .business-card {
    position: absolute;
    left: 100px;
    top: 164px;
    width: 1000px;
    height: 572px;
    background: var(--card-white);
    box-shadow: 0 6px 18px rgba(0,0,0,0.18);
    overflow: hidden;
  }
  .card-shapes {
    position: absolute;
    inset: 0;
  }
  .shape-blue { fill: var(--accent-blue); }
  .shape-grey { fill: var(--panel-grey); }
  .employee-block {
    position: absolute;
    left: 58px;
    top: 104px;
    color: var(--ink-dark);
    text-align: right;
  }
  .employee-name {
    font-size: 42px;
    font-weight: 400;
    letter-spacing: -0.5px;
    line-height: 1;
    margin: 0;
  }
  .employee-position {
    font-size: 22px;
    line-height: 1;
    margin: 2px 0 0;
  }
  .contact-list {
    position: absolute;
    left: 56px;
    top: 338px;
    margin: 0;
    padding: 0;
    list-style: none;
    color: var(--ink-light);
    font-size: 23px;
    line-height: 34px;
  }
  .contact-item {
    display: flex;
    align-items: center;
  }
  .contact-icon {
    width: 26px;
    height: 26px;
    margin-right: 20px;
    fill: var(--ink-light);
    stroke: var(--ink-light);
  }
  .brand-lockup {
    position: absolute;
    left: 600px;
    top: 220px;
    width: 340px;
    display: flex;
    flex-direction: column;
    align-items: center;
  }
  .brand-mark {
    width: 78px;
    height: 78px;
    border-radius: 50%;
    background: var(--brand-blue);
    margin-bottom: 18px;
  }
  .brand-name {
    font-size: 56px;
    font-weight: 600;
    color: var(--brand-blue);
    letter-spacing: 1px;
    margin: 0;
    line-height: 1;
  }
</style>
</head>
<body>
  <div class="business-card">
    <svg class="card-shapes" width="1000" height="572" viewBox="0 0 1000 572">
      <polygon class="shape-blue" points="0,0 480,0 405,262 0,205"/>
      <polygon class="shape-grey" points="0,205 405,262 600,572 0,572"/>
    </svg>

    <div class="employee-block">
      <p class="employee-name">EMPLOYEE NAME</p>
      <p class="employee-position">Position</p>
    </div>

    <ul class="contact-list">
      <li class="contact-item">
        <svg class="contact-icon" viewBox="0 0 26 26" stroke-width="0">
          <path d="M3 8c0-3 4-5 10-5s10 2 10 5v2h-5V8c-1-1-3-1-5-1s-4 0-5 1v2H3z"/>
          <path d="M6 12h14l3 11H3z M10 15a3 3 0 1 0 6 0a3 3 0 1 0-6 0" fill-rule="evenodd"/>
        </svg>
        MD: 555-210-0040
      </li>
      <li class="contact-item">
        <svg class="contact-icon" viewBox="0 0 26 26" stroke-width="0">
          <path d="M8 1h10a2 2 0 0 1 2 2v20a2 2 0 0 1-2 2H8a2 2 0 0 1-2-2V3a2 2 0 0 1 2-2zM8 4v16h10V4z" fill-rule="evenodd"/>
        </svg>
        DE: 555-438-0040
      </li>
      <li class="contact-item">
        <svg class="contact-icon" viewBox="0 0 26 26" stroke-width="0">
          <path d="M7 2h10l3 3v5H7z"/>
          <path d="M3 11h20v10H3z M6 14v3h8v-3z" fill-rule="evenodd"/>
          <path d="M5 22h16v2H5z"/>
        </svg>
        Fax: 555-210-0050
      </li>
      <li class="contact-item">
        <svg class="contact-icon" viewBox="0 0 26 26" stroke-width="0">
          <path d="M2 6h22v15H2z M4 8l9 7 9-7z" fill-rule="evenodd"/>
        </svg>
        E-mail: dana@torvique.com
      </li>
      <li class="contact-item">
        <svg class="contact-icon" viewBox="0 0 26 26" fill="none" stroke-width="2">
          <circle cx="13" cy="13" r="10.5"/>
          <ellipse cx="13" cy="13" rx="4.5" ry="10.5"/>
          <path d="M2.5 13h21M4.5 7.5h17M4.5 18.5h17"/>
        </svg>
        Web: www.torvique.com
      </li>
    </ul>

    <div class="brand-lockup">
      <div class="brand-mark"></div>
      <p class="brand-name">TORVIQUE</p>
    </div>
  </div>
</body>
</html>
```